IT Services company

we want a modern card design that combines business and technology whilst not being too loud

the Company Name is Corvane Hub and i have attached the logo

can you also put the words Business Enabled Technology under the logo

thanks

Hi can you please show the card with a web url and contact name and email and phone number please

Business

```html
<!DOCTYPE html>
<html lang="en">
<head>
<meta charset="utf-8">
<title>Corvane Hub — Business Card</title>
<link href="https://fonts.googleapis.com/css2?family=PT+Sans:wght@700&display=swap" rel="stylesheet">
<style>
  :root {
    --stage: #2c2c29;
    --card-white: #ffffff;
    --brand-red: #a11f25;
    --brand-blue: #22378f;
    --pattern-blue: #3a4989;
    --pattern-mid: #6b4872;
    --pattern-red: #94343b;
    --ink: #111111;
  }
  * { margin: 0; padding: 0; box-sizing: border-box; }
  html, body {
    width: 1200px;
    height: 778px;
    overflow: hidden;
    background: var(--stage);
  }
  .stage {
    position: relative;
    width: 1200px;
    height: 778px;
  }
  .business-card {
    position: absolute;
    left: 50px;
    top: 83px;
    width: 1100px;
    height: 612px;
    display: flex;
    flex-direction: column;
    background: var(--card-white);
    overflow: hidden;
  }
  .pattern-band {
    width: 100%;
    background: linear-gradient(120deg,
      var(--pattern-blue) 0%,
      var(--pattern-mid) 50%,
      var(--pattern-red) 100%);
  }
  .pattern-band--top { height: 176px; }
  .pattern-band--bottom { height: 192px; }
  .identity-band {
    position: relative;
    height: 244px;
    background: var(--card-white);
    box-shadow: 0 4px 10px rgba(0,0,0,0.25), 0 -4px 10px rgba(0,0,0,0.25);
    z-index: 1;
  }
  .brand-lockup {
    position: absolute;
    left: 229px;
    top: 39px;
    display: flex;
    align-items: center;
    gap: 36px;
  }
  .brand-mark {
    width: 136px;
    height: 136px;
    flex: none;
  }
  .brand-name {
    font-family: "PT Sans", sans-serif;
    font-weight: 700;
    font-size: 66px;
    letter-spacing: 3px;
    color: var(--brand-red);
    line-height: 1;
  }
  .tagline {
    position: absolute;
    left: 0;
    right: 0;
    top: 192px;
    text-align: center;
    font-family: "PT Sans", sans-serif;
    font-weight: 700;
    font-size: 27px;
    color: var(--ink);
    line-height: 1;
  }
</style>
</head>
<body>
  <main class="stage">
    <section class="business-card">
      <div class="pattern-band pattern-band--top" role="img" aria-label="Diagonal red, white and blue interlocking stripe pattern"></div>
      <div class="identity-band">
        <div class="brand-lockup">
          <svg class="brand-mark" viewBox="0 0 136 136" aria-hidden="true">
            <circle cx="68" cy="68" r="68" fill="var(--brand-red)"/>
          </svg>
          <h1 class="brand-name">Corvane Hub</h1>
        </div>
        <p class="tagline">Business Enabled Technology</p>
      </div>
      <div class="pattern-band pattern-band--bottom" role="img" aria-label="Diagonal red, white and blue interlocking stripe pattern"></div>
    </section>
  </main>
</body>
</html>
```